Business Card Design Project

We need business cards for the new company Venture Loom based in Abu Dhabi, UAE, which provides IT retail solutions to businesses
Design should be done as a template, so we can add people when needed.
Please see attached details.
The brief is about 2 companies from our group. We need a business card only for Venture Loom
Industry/Entity Type
Retail
Look and feel
Each slider illustrates characteristics of the customer's brand and the style your logo design should communicate.

```html
<!DOCTYPE html>
<html lang="en">
<head>
<meta charset="utf-8">
<title>Venture Loom — Business Card</title>
<link href="https://fonts.googleapis.com/css2?family=Open+Sans:wght@400;600&family=Noto+Naskh+Arabic:wght@400&display=swap" rel="stylesheet">
<style>
  :root {
    --purple: #6a52a3;
    --gold: #d9a823;
    --white: #ffffff;
    --stage: #d6d6d6;
    --ink-soft: #7a7a7a;
  }
  * { margin: 0; padding: 0; box-sizing: border-box; }
  html, body { width: 1200px; height: 900px; overflow: hidden; }
  body {
    background: var(--stage);
    font-family: "Open Sans", Arial, sans-serif;
    position: relative;
  }
  .card {
    position: absolute;
    width: 535px;
    height: 301px;
    overflow: hidden;
  }
  .card-front { left: 47px; top: 297px; background: var(--white); }
  .card-back  { left: 609px; top: 292px; background: var(--purple); }

  .top-rule {
    position: absolute; left: 0; right: 0; top: 17px;
    height: 2px; background: var(--purple);
  }
  .brand {
    position: absolute;
    display: flex; align-items: center; gap: 10px;
    font-family: "Open Sans", Arial, sans-serif;
    font-weight: 600;
    white-space: nowrap;
  }
  .brand-front { left: 18px; top: 180px; color: var(--purple); font-size: 28px; }
  .brand-front .brand-dot { width: 14px; height: 14px; border-radius: 50%; background: var(--purple); }
  .brand-back { right: 22px; bottom: 20px; color: var(--white); font-size: 34px; }
  .brand-back .brand-dot { width: 16px; height: 16px; border-radius: 50%; background: var(--white); }

  .details { position: absolute; left: 249px; top: 76px; width: 276px; }
  .person-name {
    color: var(--gold); font-size: 19px; font-weight: 400; letter-spacing: 0.2px;
    line-height: 24px;
  }
  .person-name-ar, .job-title-ar {
    font-family: "Noto Naskh Arabic", serif;
    direction: rtl; text-align: left;
  }
  .person-name-ar { color: var(--gold); font-size: 17px; line-height: 22px; width: 228px; text-align: right; }
  .job-title { color: var(--purple); font-size: 11.5px; margin-top: 12px; line-height: 16px; }
  .job-title-ar { color: var(--purple); font-size: 13.5px; line-height: 20px; width: 145px; text-align: right; }

  .contact { margin-top: 20px; list-style: none; }
  .contact li { color: var(--purple); font-size: 11.5px; line-height: 18px; white-space: nowrap; }
  .contact .label { color: var(--gold); font-weight: 600; }

  .address-band {
    position: absolute; left: 0; right: 0; bottom: 0; height: 26px;
    background: var(--purple); color: var(--white);
    font-size: 11.5px; letter-spacing: 1px; text-align: center; line-height: 26px;
  }
</style>
</head>
<body>
  <section class="card card-front" aria-label="Business card front">
    <div class="top-rule"></div>
    <div class="brand brand-front"><span class="brand-dot"></span>Venture Loom</div>
    <div class="details">
      <p class="person-name">KARIM HADDAD</p>
      <p class="person-name-ar">كريم حداد</p>
      <p class="job-title">Retail Solutions Manager</p>
      <p class="job-title-ar">مدير حلول البيع بالتجزئة</p>
      <ul class="contact">
        <li><span class="label">T:</span> +971 2 480 3300 &nbsp;-&nbsp; Ext: 214</li>
        <li><span class="label">M:</span> +971 55 301 7742 &nbsp;-&nbsp; <span class="label">F:</span> +971 2 480 3310</li>
        <li><span class="label">E:</span> k.haddad@ventureloom.ae &nbsp;-&nbsp; <span class="label">W:</span> ventureloom.ae</li>
      </ul>
    </div>
    <div class="address-band">PO BOX 51820, ABU DHABI, UAE</div>
  </section>

  <section class="card card-back" aria-label="Business card back">
    <div class="brand brand-back"><span class="brand-dot"></span>Venture Loom</div>
  </section>
</body>
</html>
```